Millbrook Dental Center Letterhead

We need letterhead. Attached is the business card info and style that we want to incorporate into the letterhead. I want 2 forms of the letterlead. First, standard letterhead and second, I want the same thing, but with the tree almost translucent on the page. I need 8.5x11. I want color similar to the blue and brown that is on the business card. I like the wave simailar to the card also. Across the bottom as a ticker tape should list the treatments available.

Requirements
Must have
• Colors, layout, logos and info that is on the business card.

```html
<!DOCTYPE html>
<html lang="en">
<head>
<meta charset="utf-8">
<title>Millbrook Dental Center Letterhead</title>
<link href="https://fonts.googleapis.com/css2?family=Open+Sans:wght@400;600;700&display=swap" rel="stylesheet">
<style>
  :root {
    --canvas: #ffffff;
    --paper-light: #fbfbfc;
    --paper-dark: #e2e4e6;
    --teal: #3e5f69;
    --brand-blue: #4a7d8e;
    --brand-brown: #6b5a4a;
    --tree-tint: #dfe3e6;
    --on-teal: #e8eef0;
  }
  * { box-sizing: border-box; margin: 0; padding: 0; }
  html, body {
    width: 1200px; height: 785px; overflow: hidden;
    background: var(--canvas);
    font-family: "Open Sans", Arial, sans-serif;
  }
  .sheet-set { position: relative; width: 1200px; height: 785px; }
  .letterhead {
    position: absolute; top: 2px; width: 552px; height: 780px;
    background: linear-gradient(180deg, var(--paper-light) 0%, #eef0f1 55%, var(--paper-dark) 100%);
    box-shadow: 0 1px 4px rgba(0,0,0,0.18);
    overflow: hidden;
  }
  .letterhead--standard { left: 2px; }
  .letterhead--watermark { left: 644px; }

  .brand {
    position: absolute; top: 30px; left: 356px;
    display: flex; align-items: center; gap: 7px;
  }
  .brand__dot {
    width: 16px; height: 16px; border-radius: 50%;
    background: var(--brand-blue); flex: none;
  }
  .brand__name {
    font-weight: 600; font-size: 13px; line-height: 1.1;
    color: var(--brand-blue); white-space: nowrap;
  }
  .brand__tagline {
    margin-top: 3px; font-size: 6.5px; font-weight: 600;
    letter-spacing: 0.9px; color: var(--brand-brown); white-space: nowrap;
  }

  .tree-watermark {
    position: absolute; left: 40px; top: 140px; width: 490px; height: 550px;
    background: radial-gradient(ellipse at 50% 45%, var(--tree-tint) 0%, rgba(223,227,230,0.55) 45%, rgba(223,227,230,0) 72%);
  }

  .wave { position: absolute; left: 0; bottom: 0; width: 552px; height: 118px; display: block; }
  .wave path { fill: var(--teal); }

  .contact {
    position: absolute; left: 16px; right: 16px; bottom: 22px;
    display: flex; justify-content: space-between; align-items: flex-end;
    color: var(--on-teal); font-size: 8.5px; font-weight: 600; line-height: 1.6;
  }
  .contact__address { font-style: normal; }
  .contact__web { text-align: right; }
</style>
</head>
<body>
<main class="sheet-set">

  <section class="letterhead letterhead--standard" aria-label="Standard letterhead">
    <header class="brand">
      <span class="brand__dot" aria-hidden="true"></span>
      <div>
        <p class="brand__name">Millbrook Dental Center</p>
        <p class="brand__tagline">GENTLE CARE FOR EVERY SMILE</p>
      </div>
    </header>
    <svg class="wave" viewBox="0 0 552 118" preserveAspectRatio="none" aria-hidden="true">
      <path d="M0 26 C100 6 185 16 270 32 C370 50 465 46 552 20 L552 118 L0 118 Z"/>
    </svg>
    <footer class="contact">
      <address class="contact__address">2417 Aspen Ridge Dr. Suite 120<br>Millbrook Springs, CO 80000</address>
      <p class="contact__phones">(555) 014-2096<br>(555) 014-3758</p>
      <p class="contact__web">hello@millbrookdental.com<br>www.millbrookdentalcenter.com</p>
    </footer>
  </section>

  <section class="letterhead letterhead--watermark" aria-label="Letterhead with translucent tree">
    <header class="brand">
      <span class="brand__dot" aria-hidden="true"></span>
      <div>
        <p class="brand__name">Millbrook Dental Center</p>
        <p class="brand__tagline">GENTLE CARE FOR EVERY SMILE</p>
      </div>
    </header>
    <div class="tree-watermark" role="img" aria-label="Large translucent tree watermark in pale grey"></div>
    <svg class="wave" viewBox="0 0 552 118" preserveAspectRatio="none" aria-hidden="true">
      <path d="M0 40 C90 14 185 22 270 36 C370 52 465 50 552 26 L552 118 L0 118 Z"/>
    </svg>
  </section>

</main>
</body>
</html>
```